Womans Supplement Designs

Launching a Supplement company and need to get some initial designs created, I've attached our logo and the bottle type that I want the samples done one.

This project is for our Whey Protein we are starting with Vanilla, chocolate and strawberry banana

(ALL DESIGN VARIATIONS MUST BE A WHITE BOTTLE NOT BLACK)

(FOR DESIGN SAMPLES PLEASE USE THE SUPPLEMENT BOTTLE STYLE I PROVIDED)

Whoever is selected the winner I will have more work for you to complete the disigns for the rest of the products in the line, Just want to get this shake completed first

Target Market(s)

Women

Requirements
Must have
• Must have our current logo involved

the name of this product will be "KIVA LUM"

Must have this slogan,

ALL-IN-ONE PREMIUM PROTEIN NUTRITIONAL SHAKE FOR BLACK WOMEN

This is our meal replacement

the design should try to keep the same look and feel of the existing provided supplement images

we are starting with chocolate, vanilla and strawberry banana

this is for women and should look colorful and appeal to them
Should not have
• Do not use an image of a person or lady, don't want it branded to a person

```html
<!DOCTYPE html>
<html lang="en">
<head>
<meta charset="utf-8">
<title>Kiva Lum – Chocolate Protein Shake Label</title>
<link rel="stylesheet" href="https://fonts.googleapis.com/css2?family=Roboto+Condensed:wght@400;500;700&family=Roboto:wght@700&display=swap">
<style>
  :root {
    --ink: #111111;
    --cocoa: #a0582a;
    --paper: #ffffff;
    --on-cocoa: #ffffff;
  }
  html, body {
    margin: 0;
    padding: 0;
    overflow: hidden;
  }
  body {
    width: 1164px;
    height: 1200px;
    background: var(--paper);
  }
  .label {
    position: relative;
    width: 1164px;
    height: 1200px;
    display: flex;
    flex-direction: column;
    align-items: center;
    color: var(--ink);
  }
  .brand {
    margin-top: 300px;
    display: flex;
    align-items: center;
    gap: 18px;
    font-family: "Roboto Condensed", sans-serif;
    font-weight: 500;
    font-size: 40px;
    letter-spacing: 0.18em;
    color: var(--ink);
  }
  .brand-mark {
    width: 22px;
    height: 22px;
    background: var(--ink);
  }
  .product-name {
    margin: 180px 0 0;
    font-family: "Roboto Condensed", sans-serif;
    font-weight: 700;
    font-size: 150px;
    line-height: 1;
    letter-spacing: -0.01em;
  }
  .divider {
    width: 540px;
    height: 7px;
    margin-top: 34px;
    background: var(--cocoa);
  }
  .slogan {
    margin: 26px 0 0;
    font-family: "Roboto Condensed", sans-serif;
    font-weight: 400;
    font-size: 46px;
    line-height: 58px;
    text-align: center;
    letter-spacing: -0.01em;
  }
  .flavour {
    margin-top: 58px;
    width: 414px;
    height: 64px;
    display: flex;
    align-items: center;
    justify-content: center;
    background: var(--cocoa);
    color: var(--on-cocoa);
    font-family: "Roboto", sans-serif;
    font-weight: 700;
    font-size: 36px;
    letter-spacing: 0.2em;
    padding-left: 0.2em;
    box-sizing: border-box;
  }
</style>
</head>
<body>
  <main class="label">
    <div class="brand">
      <span class="brand-mark" aria-hidden="true"></span>
      <span class="brand-name">SELA RIVE NUTRITION</span>
    </div>
    <h1 class="product-name">KIVA LUM</h1>
    <div class="divider" aria-hidden="true"></div>
    <p class="slogan">ALL-IN-ONE PREMIUM<br>PROTEIN NUTRITIONAL SHAKE<br>FOR BLACK WOMEN</p>
    <div class="flavour">CHOCOLATE</div>
  </main>
</body>
</html>
```